UX interface for a Crypto currency payment gateway

This project requires you to open an account on our development web site http://dev.quorvan.com/cgi-bin/d

It requires you, as well, to download and install a Bitcoin client working on the testnet network (such as electrum), then get some Bitcoin testnet (those are free for who knows how to get them). "Simulate a payment" works as well.

This project requires you to know how to work with Bitcoins and cryptocurrencies.

Do NOT submit work if you're not interested in crypto-currencies.

Then, make some simulated payments on our development web site (Bitcoin testnet is only one supported crypto-currency there) to fill up a little bit the transaction report and the wallets.

Our UX sucks, yep, I know that, that's why we need you !

Then propose a design for the back office, first page is good enough (Accounts & Wallets).

You can change the layout as you see fit, the contest is as much about the UX design than the graphic design.

The price of the contest is for the best design of the first page only (Accounts & Wallets).

However, the winner will be required to code his design in HTML/CSS (JS may be required as well depending on your design) and he will get the whole back office and check out page to design and code in a one to one relationship with the customer (be prepared for a long term project). The winner will integrate his coding inside our templates.

Do NOT submit work if you're not interested to take the whole project or if you're not able to dedicate enough time to deliver a big quantity of work fast.

Number of Pages Required

1 page

Font styles to use
Sans Serif

Requirements
Must have
• Design must look professional in "bank" style.

```html
<!DOCTYPE html>
<html lang="en">
<head>
<meta charset="utf-8">
<title>LedgerGate — Accounts &amp; Wallet</title>
<link href="https://fonts.googleapis.com/css2?family=Nunito+Sans:wght@400;600;700&display=swap" rel="stylesheet">
<style>
:root{
  --frame:#1c1c1c;
  --ink:#3a3f44;
  --muted:#9aa1a6;
  --faint:#c3c8cc;
  --green:#068330;
  --green-dark:#0a7a2c;
  --lime:#8cc63f;
  --lime-light:#b6d95a;
  --side:#4f5d62;
  --side-band:#6c787c;
  --red:#f1505a;
  --yellow:#f7d46a;
  --line:#e4e6e8;
}
*{box-sizing:border-box;margin:0;padding:0}
html,body{width:1200px;height:1200px;overflow:hidden}
body{background:var(--frame);font-family:"Nunito Sans",sans-serif;color:var(--ink);position:relative}
.abs{position:absolute}
.app{position:absolute;left:0;top:100px;width:1200px;height:1000px;overflow:hidden;
  background:linear-gradient(90deg,#b5d86a 0%,#d8ecb0 25%,#eef7d6 42%,#a9d3b4 62%,#b9dcae 80%,#a9d692 100%)}
/* header */
.topbar{position:absolute;left:0;top:0;width:1200px;height:50px;background:#fff;box-shadow:0 1px 3px rgba(0,0,0,.08)}
.brand{position:absolute;left:40px;top:16px;font-size:14px;font-weight:700;letter-spacing:.5px;color:var(--ink);display:flex;align-items:center;gap:6px}
.brand-mark{width:10px;height:10px;border-radius:50%;background:var(--green)}
.nav a{position:absolute;top:17px;font-size:11.5px;color:#555;text-decoration:none}
.nav a.active{color:var(--green);font-weight:600}
.nav a.active::after{content:"";position:absolute;left:0;right:0;top:30px;height:2px;background:var(--green)}
.search{position:absolute;left:701px;top:8px;width:206px;height:34px;border-radius:17px;background:#f1f2f3;border:1px solid #e1e3e5;font-size:9.5px;color:#b6bbbf;padding:10px 0 0 28px}
.search svg{position:absolute;right:14px;top:11px}
.avatar{position:absolute;left:946px;top:10px;width:30px;height:30px;border-radius:50%;background:linear-gradient(#f3b27a,#e36a3a);border:2px solid #eee}
.greet{position:absolute;left:982px;top:19px;font-size:8.5px;color:#444}
.bell{position:absolute;left:1072px;top:16px}
.badge{position:absolute;left:1078px;top:13px;width:9px;height:9px;border-radius:50%;background:var(--green);color:#fff;font-size:6px;text-align:center;line-height:9px}
.settings{position:absolute;left:1104px;top:16px;font-size:8.5px;color:#444;display:flex;gap:6px;align-items:center}
/* sidebar */
.sidebar{position:absolute;left:0;top:50px;width:153px;height:926px;background:var(--side);color:#fff}
.side-band{position:absolute;left:0;width:153px;height:40px;background:var(--side-band);font-size:15px;text-align:center;line-height:40px}
.side-item{position:absolute;left:35px;font-size:12px;color:#f2f4f4}
.side-item svg{position:absolute;left:-25px;top:0}
.profile{position:absolute;left:24px;top:463px;font-size:12px;font-weight:600}
.label-field{position:absolute;left:16px;top:500px;width:120px;height:22px;border:1px solid #8d989b;border-radius:11px;font-size:8px;padding:5px 10px}
.record-btn{position:absolute;left:16px;top:535px;width:120px;height:22px;border-radius:11px;background:var(--green);font-size:8px;text-align:center;line-height:22px;font-weight:600}
/* sections */
.section-title{position:absolute;top:80px;font-size:15px;color:#4a5156}
.card{position:absolute;background:#fff;border-radius:3px;box-shadow:0 2px 6px rgba(0,0,0,.06)}
.wallet-card{left:168px;top:116px;width:554px;height:283px}
.balance-card{left:733px;top:116px;width:218px;height:283px}
.value-card{left:960px;top:116px;width:219px;height:283px}
.tip{position:absolute;background:#fff;border-radius:3px;box-shadow:0 2px 8px rgba(0,0,0,.1);text-align:center;font-size:11px;color:#333;padding-top:9px}
.tip small{display:block;font-size:7px;margin-top:2px}
.tip .up{color:var(--green)}
.tip .up-red{color:var(--red)}
.tip .date{color:#555}
.legend{position:absolute;font-size:7.5px;color:var(--green);font-weight:600}
.summary{position:absolute;border-radius:3px;box-shadow:0 2px 6px rgba(0,0,0,.08);background:#fff;height:114px}
.summary .row{position:absolute;left:14px;right:14px;font-size:9px;display:flex;justify-content:space-between}
.row.k1{color:#333}.row.k2{color:#777}.row.k3,.row.k4{color:var(--faint)}
.view-link{position:absolute;font-size:7.5px;display:flex;align-items:center;gap:5px}
.view-link::after{content:"";width:22px;height:1px;background:currentColor}
/* table */
.table-bar{position:absolute;left:168px;top:413px;width:1013px;height:37px;background:var(--green)}
.tag-search{position:absolute;left:24px;top:9px;width:119px;height:20px;border-radius:10px;background:#fff;font-size:7.5px;padding:5px 9px;color:#444}
.tag-search svg{position:absolute;right:9px;top:6px}
.more-btn{position:absolute;left:867px;top:0;width:115px;height:37px;background:var(--lime);color:#fff;font-size:8px;padding:14px 12px}
.gear-btn{position:absolute;left:982px;top:0;width:31px;height:37px;background:var(--green-dark)}
.tx-table{position:absolute;left:168px;top:450px;width:1013px;height:522px;background:#fff}
.tx-head{position:absolute;left:0;top:0;width:1013px;height:28px;background:#e8e9ea;font-size:8.5px;color:#444}
.tx-head span{position:absolute;top:9px}
.col-sep{position:absolute;top:28px;bottom:4px;width:1px;background:var(--line)}
.tx-row{position:absolute;left:0;width:1013px;height:31px;font-size:8.5px;color:#444}
.tx-row span{position:absolute;top:0}
.tx-row .info{font-size:7px}
.bottom-band{position:absolute;left:0;top:976px;width:1200px;height:24px;background:linear-gradient(90deg,#a6d14a,#e9f5c8 40%,#b5dba4 100%)}
</style>
</head>
<body>
<div class="app">
  <div class="bottom-band"></div>
  <header class="topbar">
    <div class="brand"><span class="brand-mark"></span>LEDGERGATE</div>
    <nav class="nav">
      <a class="active" style="left:278px">Accounts &amp; Wallet</a>
      <a style="left:456px">Get Paid</a>
      <a style="left:586px">Send &amp; Receive</a>
    </nav>
    <div class="search">Search your account details
      <svg width="11" height="11" viewBox="0 0 11 11"><circle cx="4.5" cy="4.5" r="3.6" fill="none" stroke="#555" stroke-width="1.3"/><path d="M7.3 7.3L10 10" stroke="#555" stroke-width="1.3"/></svg></div>
    <div class="avatar" role="img" aria-label="User avatar"></div>
    <div class="greet">Hi, Daniel Shore ▾</div>
    <svg class="bell" width="13" height="14" viewBox="0 0 13 14"><path d="M2 10V6a4.5 4.5 0 019 0v4l1 1H1z M5 12.5h3" fill="none" stroke="#666" stroke-width="1"/></svg>
    <div class="badge">1</div>
    <div class="settings"><svg width="14" height="14" viewBox="0 0 14 14"><circle cx="7" cy="7" r="2.3" fill="none" stroke="#555"/><circle cx="7" cy="7" r="5.3" fill="none" stroke="#555" stroke-dasharray="2 1.2"/></svg>Settings</div>
  </header>

  <aside class="sidebar">
    <div class="side-band" style="top:28px">Get Paid</div>
    <div class="side-item" style="top:96px"><svg width="14" height="13"><path d="M1 12h12M3 11V7M6 11V5M9 11V3M12 11V1" stroke="#fff" stroke-width="1"/></svg>Simulate a payment</div>
    <div class="side-item" style="top:129px"><svg width="14" height="13"><rect x="1" y="1" width="12" height="11" fill="none" stroke="#fff"/><path d="M3 4h3M3 7h3M8 4h3M8 7h3" stroke="#fff"/></svg>Generate invoice</div>
    <div class="side-item" style="top:163px"><svg width="15" height="13"><path d="M4 10H3a2.5 2.5 0 010-5 4 4 0 017.5-1A3 3 0 0112 10h-1M7.5 12V6M5.5 8l2-2 2 2" fill="none" stroke="#fff"/></svg>Upload invoice</div>
    <div class="side-band" style="top:295px">Accounts</div>
    <div class="profile">Daniel Shore <svg width="11" height="11" style="margin-left:16px"><path d="M1 10l1-3 6-6 2 2-6 6z" fill="none" stroke="#fff"/></svg></div>
    <div class="label-field">Label</div>
    <div class="record-btn">Record New Account</div>
  </aside>

  <div class="section-title" style="left:178px">Wallets</div>
  <div class="section-title" style="left:733px">Balance</div>
  <div class="section-title" style="left:960px">Value</div>

  <!-- wallet chart -->
  <section class="card wallet-card">
    <div class="abs" style="left:38px;top:20px;font-size:12px;color:#444">Currency ▾</div>
    <div class="legend" style="left:114px;top:23px;display:flex;align-items:center;gap:5px"><span style="width:7px;height:7px;border-radius:50%;background:var(--green)"></span>Bitcoin</div>
    <div class="legend" style="left:170px;top:23px;color:var(--lime);display:flex;align-items:center;gap:5px"><span style="width:7px;height:7px;border-radius:50%;background:var(--lime)"></span>Ether</div>
    <div class="abs" style="left:525px;top:14px;color:#bbb;font-size:12px;letter-spacing:1px">•••</div>
    <svg class="abs" style="left:0;top:0" width="554" height="283" viewBox="0 0 554 283">
      <g stroke="#e2e4e6" stroke-dasharray="3 5">
        <line x1="42" y1="60" x2="512" y2="60"/><line x1="42" y1="89" x2="512" y2="89"/>
        <line x1="42" y1="123" x2="512" y2="123"/><line x1="42" y1="157" x2="512" y2="157"/>
        <line x1="42" y1="190" x2="512" y2="190"/>
      </g>
      <g font-size="7" fill="#b9bec2" font-family="Nunito Sans, sans-serif">
        <text x="42" y="92">8K</text><text x="42" y="126">6K</text><text x="42" y="160">4K</text><text x="42" y="193">2K</text><text x="42" y="227">0</text>
      </g>
      <g font-size="7" fill="#b9bec2" text-anchor="middle" font-family="Nunito Sans, sans-serif">
        <text x="68" y="239">Mon</text><text x="68" y="250">13</text>
        <text x="99" y="239">Tue</text><text x="97" y="250">14</text>
        <text x="136" y="239">Wed</text><text x="131" y="250">15</text>
        <text x="174" y="239">Thu</text><text x="172" y="250">16</text>
        <text x="212" y="239">Fri</text><text x="212" y="250">17</text>
        <text x="250" y="239">Sat</text><text x="248" y="250">18</text>
        <text x="288" y="239">Sun</text><text x="285" y="250">19</text>
        <text x="325" y="239">Mon</text><text x="322" y="250">20</text>
        <text x="364" y="239">Tue</text><text x="362" y="250">21</text>
        <text x="401" y="239">Wed</text><text x="397" y="250">22</text>
        <text x="439" y="239">Thu</text><text x="439" y="250">23</text>
        <text x="477" y="239">Fri</text><text x="477" y="250">24</text>
        <text x="515" y="239">Sat</text><text x="513" y="250">25</text>
      </g>
      <circle cx="172" cy="256" r="1.8" fill="var(--green)"/><circle cx="248" cy="256" r="1.8" fill="var(--lime)"/>
      <g fill="none">
        <circle cx="341" cy="62" r="28" stroke="#e3f0e6" stroke-width="3"/><circle cx="341" cy="62" r="19" stroke="#d2e8d6" stroke-width="2"/><circle cx="341" cy="62" r="11" stroke="#c4e1ca" stroke-width="2"/>
        <circle cx="434" cy="113" r="28" stroke="#eef5da" stroke-width="3"/><circle cx="434" cy="113" r="19" stroke="#e3efc4" stroke-width="2"/><circle cx="434" cy="113" r="11" stroke="#d8e9ae" stroke-width="2"/>
      </g>
      <path d="M66 188C88 166 110 160 130 162C165 166 190 186 230 178C265 171 285 140 320 141C365 142 400 140 434 113" fill="none" stroke="var(--lime-light)" stroke-width="3.5"/>
      <path d="M64 174C95 200 130 222 170 220C215 218 250 200 280 165C305 135 325 95 341 62" fill="none" stroke="var(--green)" stroke-width="2.5"/>
      <circle cx="341" cy="62" r="3.5" fill="var(--green)"/><circle cx="434" cy="113" r="3.5" fill="var(--lime)"/>
    </svg>
  </section>
  <div class="tip" style="left:492px;top:106px;width:87px;height:54px">5.020,00<small class="up">▲ 120,00</small><small class="date">5 June , 2018</small></div>
  <div class="tip" style="left:586px;top:162px;width:86px;height:52px">2.215,00<small class="up" style="color:var(--lime)">▲ 95.00</small><small class="date">5 June , 2018</small></div>

  <!-- balance -->
  <section class="card balance-card">
    <svg class="abs" style="left:10px;top:30px" width="110" height="110" viewBox="0 0 110 110">
      <path d="M14 82A47 47 0 0 1 80 16" fill="none" stroke="var(--yellow)" stroke-width="6"/>
      <path d="M20 74A42 42 0 1 1 98 74" fill="none" stroke="var(--red)" stroke-width="5" transform="rotate(30 55 58)"/>
      <circle cx="55" cy="58" r="36" fill="none" stroke="#e1e3e5" stroke-width="4"/>
      <path d="M25 50A32 32 0 0 1 86 48" fill="none" stroke="#3e4347" stroke-width="4"/>
    </svg>
    <div class="abs" style="left:123px;top:158px"></div>
    <div class="legend" style="left:135px;top:154px;color:#333;font-size:9.5px;font-weight:400;line-height:18px">
      <div><span style="color:var(--yellow)">●</span>&nbsp;&nbsp; BTC</div>
      <div><span style="color:var(--red)">●</span>&nbsp;&nbsp; ETH</div>
      <div><span style="color:#3e4347">●</span>&nbsp;&nbsp; INVESTED</div>
      <div><span style="color:#d6d9db">●</span>&nbsp;&nbsp; TOTAL</div>
    </div>
    <div class="summary" style="left:11px;top:154px;width:196px;border-bottom:2px solid #f6c9cc">
      <div class="row k1" style="top:12px"><span>BTC</span><span>00.22120..05153</span></div>
      <div class="row k2" style="top:37px"><span>ETH</span><span>12548.5154</span></div>
      <div class="row k3" style="top:62px"><span>INVESTED</span><span>64549133</span></div>
      <div class="row k4" style="top:88px"><span>TOTAL</span><span>894566623</span></div>
    </div>
    <div class="view-link" style="left:139px;top:274px;color:var(--red)">View Details</div>
  </section>
  <div class="tip" style="left:790px;top:98px;width:87px;height:55px">64548951<small class="up-red">▲ 15.200</small><small class="date">5 June , 2018</small></div>

  <!-- value -->
  <section class="card value-card">
    <div class="abs" style="left:63px;top:18px;font-size:9.5px">Bitcoin</div>
    <div class="abs" style="left:128px;top:18px;font-size:9.5px">Ether</div>
    <svg class="abs" style="left:57px;top:38px" width="110" height="110" viewBox="0 0 110 110">
      <path d="M0 0h42v14h-17l-4 5-4-5H0z" fill="var(--green)"/><path d="M0 14L42 4v10z" fill="#2ea04e"/>
      <g fill="var(--green)">
        <rect y="28" width="42" height="2.5"/><rect y="34.5" width="42" height="2.5"/><rect y="41" width="42" height="2.5"/><rect y="47.5" width="42" height="2.5"/><rect y="54" width="42" height="2.5"/><rect y="60.5" width="42" height="2.5"/><rect y="67" width="42" height="2.5"/><rect y="73.5" width="42" height="2.5"/><rect y="80" width="42" height="2.5"/><rect y="86.5" width="42" height="2.5"/>
      </g>
      <path d="M63 0h42v14H88l-4 5-4-5H63z" fill="var(--lime)"/><path d="M63 14l42-10v10z" fill="#a6d35c"/>
      <g fill="var(--lime-light)">
        <rect x="63" y="28" width="42" height="2.5"/><rect x="63" y="34.5" width="42" height="2.5"/><rect x="63" y="41" width="42" height="2.5"/><rect x="63" y="47.5" width="42" height="2.5"/><rect x="63" y="54" width="42" height="2.5"/>
      </g>
    </svg>
    <div class="abs" style="left:68px;top:136px;font-size:9.5px">90%</div>
    <div class="abs" style="left:129px;top:114px;font-size:9.5px">65%</div>
    <div class="summary" style="left:12px;top:154px;width:196px;border-bottom:2px solid #cfe8d3">
      <div class="row k1" style="top:12px"><span>BTC</span><span>25649.644</span></div>
      <div class="row k2" style="top:37px"><span>ETH</span><span>58649.6287</span></div>
      <div class="row k3" style="top:62px"><span>INVESTED</span><span>49742.6</span></div>
      <div class="row k4" style="top:88px"><span>TOTAL</span><span>44545549</span></div>
    </div>
    <div class="view-link" style="left:141px;top:274px;color:var(--green)">View Details</div>
  </section>

  <!-- transactions -->
  <div class="table-bar">
    <div class="tag-search">Search by tag<svg width="9" height="9"><circle cx="3.8" cy="3.8" r="2.8" fill="none" stroke="#333" stroke-width="1.2"/><path d="M6 6l2.5 2.5" stroke="#333" stroke-width="1.2"/></svg></div>
    <div class="more-btn">⊕ More</div>
    <div class="gear-btn"><svg width="31" height="37"><circle cx="15.5" cy="18.5" r="3" fill="none" stroke="#fff" stroke-width="2.2" stroke-dasharray="1.8 1"/></svg></div>
  </div>
  <section class="tx-table">
    <div class="tx-head">
      <span style="left:38px">Date ⌄</span><span style="left:151px">Customer</span><span style="left:260px">⌄</span>
      <span style="left:247px;left:250px"></span><span style="left:276px">Invoice # or Comment ⌄</span>
      <span style="left:410px">Received</span><span style="left:508px">⌄</span>
      <span style="left:547px">Invoice Amount</span><span style="left:676px">⌄</span>
      <span style="left:690px">Exchange Rate</span><span style="left:821px">⌄</span>
      <span style="left:853px">Info</span><span style="left:939px">⌄</span>
    </div>
    <div class="col-sep" style="left:121px"></div><div class="col-sep" style="left:234px"></div><div class="col-sep" style="left:379px"></div>
    <div class="col-sep" style="left:522px"></div><div class="col-sep" style="left:666px"></div><div class="col-sep" style="left:810px"></div>

    <div class="tx-row" style="top:152px"></div>
    <div class="tx-row" style="top:152px;left:0"></div>
    <div style="position:absolute;left:0;top:152px"></div>
    <div class="tx-row" style="top:152px"></div>
    <div class="tx-row" style="top:152px"></div>

    <div class="tx-row" style="top:152px"></div>
  </section>
  <section class="tx-rows abs" style="left:168px;top:450px;width:1013px;height:522px">
    <div class="tx-row" style="top:152px"></div>
  </section>
  <section class="abs" style="left:168px;top:450px;width:1013px">
    <div class="tx-row" style="top:152px"></div>
  </section>
  <section class="abs" style="left:168px;top:450px;width:1013px;height:522px">
    <div class="tx-row" style="top:52px"><span style="left:38px">04 June 2018</span><span style="left:148px">Ivan Morel</span><span style="left:250px">Uploaded</span><span style="left:410px">6455884</span><span style="left:547px">6455884 USD/K...</span><span style="left:690px">6455884 USD/K...</span><span class="info" style="left:856px">CIF</span></div>
    <div class="tx-row" style="top:83px"><span style="left:38px">02 June 2018</span><span style="left:148px">Peter Aldane</span><span style="left:250px">Printed</span><span style="left:410px">825213</span><span style="left:547px">825213 USD/K...</span><span style="left:690px">825213 USD/K...</span><span class="info" style="left:856px">CIF</span></div>
    <div class="tx-row" style="top:114px"><span style="left:38px">01 June 2018</span><span style="left:148px">Nadia Varel</span><span style="left:250px">Delivered</span><span style="left:410px">787555136</span><span style="left:547px">787555136 USD/K...</span><span style="left:690px">787555136 USD/K...</span><span class="info" style="left:856px">CIF</span></div>
    <div class="tx-row" style="top:146px"><span style="left:38px">30 May 2018</span><span style="left:148px">Elsa Brunov</span><span style="left:250px">Pending</span><span style="left:410px">545884123</span><span style="left:547px">545884123 USD/K...</span><span style="left:690px">545884123 USD/K...</span><span class="info" style="left:856px">DAT</span></div>
    <div class="tx-row" style="top:177px"><span style="left:38px">28 May 2018</span><span style="left:148px">Tessa Lindqvist</span><span style="left:250px">Uploaded</span><span style="left:356px;top:-1px;width:9px;height:7px;background:#f5c542;border-radius:1px"></span><span style="left:410px">84565123</span><span style="left:547px">84565123 USD/K...</span><span style="left:690px">84565123 USD/K...</span><span class="info" style="left:856px">DAT</span></div>
    <div class="tx-row" style="top:208px"><span style="left:38px">25 May 2018</span><span style="left:148px">Mira Holloway</span><span style="left:250px">Uploaded</span><span style="left:410px">8814556987</span><span style="left:547px">8814556987 USD/K...</span><span style="left:690px">8814556987 USD/K...</span><span class="info" style="left:856px">DAT L</span></div>
    <div class="tx-row" style="top:239px"><span style="left:38px">20 May 2018</span><span style="left:148px">Owen Castellan</span><span style="left:250px">On Process</span><span style="left:410px">6454812</span><span style="left:547px">6454812 USD/K...</span><span style="left:690px">6454812 USD/K...</span><span class="info" style="left:856px">DD</span></div>
    <div class="tx-row" style="top:271px"><span style="left:38px">17 May 2018</span><span style="left:148px">Greta Solm</span><span style="left:250px">On Process</span><span style="left:410px">8445513</span><span style="left:547px">8445513 USD/K...</span><span style="left:690px">8445513 USD/K...</span><span class="info" style="left:856px">CIF</span></div>
    <div class="tx-row" style="top:302px"><span style="left:38px">16 May 2018</span><span style="left:148px">Hugo Frane</span><span style="left:250px">On Process</span><span style="left:410px">126448984</span><span style="left:547px">126448984 USD/K...</span><span style="left:690px">126448984 USD/K...</span><span class="info" style="left:856px">CIF</span></div>
    <div class="tx-row" style="top:333px"><span style="left:38px">11 May 2018</span><span style="left:148px">Simon Darrow</span><span style="left:250px">Uploaded</span><span style="left:410px">7542313</span><span style="left:547px">7542313 USD/K...</span><span style="left:690px">7542313 USD/K...</span><span class="info" style="left:856px">DDP</span></div>
    <div class="tx-row" style="top:364px"><span style="left:38px">09 May 2018</span><span style="left:148px">Lena Vask</span><span style="left:250px">Uploaded</span><span style="left:354px;top:-1px;width:9px;height:7px;background:#f5c542;border-radius:1px"></span><span style="left:361px;top:1px;width:6px;height:6px;background:#3cb44b;border-radius:50%"></span><span style="left:410px">455123369</span><span style="left:547px">455123369 USD/K...</span><span style="left:690px">455123369 USD/K...</span><span class="info" style="left:856px">CIF</span></div>
    <div class="tx-row" style="top:396px"><span style="left:38px">07 May 2018</span><span style="left:148px">Clara Penwick</span><span style="left:250px">Pending</span><span style="left:410px">32158456</span><span style="left:547px">32158456 USD/K...</span><span style="left:690px">32158456 USD/K...</span><span class="info" style="left:856px">CIF Sa</span></div>
    <div class="tx-row" style="top:427px"><span style="left:38px">06 May 2018</span><span style="left:148px">Ruth Calder</span><span style="left:250px">Pending</span><span style="left:410px">25481236</span><span style="left:547px">25481236 USD/K...</span><span style="left:690px">25481236 USD/K...</span><span class="info" style="left:856px">FCA</span></div>
    <div class="tx-row" style="top:458px"><span style="left:38px">05 May 2018</span><span style="left:148px">Ada Kellner</span><span style="left:250px">Delivered</span><span style="left:410px">8454522</span><span style="left:547px">8454522 USD/K...</span><span style="left:690px">8454522 USD/K...</span><span class="info" style="left:856px">CIF</span></div>
    <div class="tx-row" style="top:489px"><span style="left:38px">03 May 2018</span><span style="left:148px">Leo Marsden</span><span style="left:250px">Delivered</span><span style="left:410px">754223699</span><span style="left:547px">754223699 USD/K...</span><span style="left:690px">754223699 USD/K...</span><span class="info" style="left:856px">DAP</span></div>
    <div class="view-link" style="left:922px;top:507px;color:var(--lime)">View Details</div>
  </section>
</div>
</body>
</html>
```